Cell Tower company needs website updated

We need a website that does not look like it was designed in the early 1990's. The company fabricates, installs and reinforces communication towers throughout the US, Caribbean, Central and S. America. We are located in Pensacola Florida. Our tower technicians travel to wherever the work is. I have some good pictures taken from towers to use on the site. I want the site to reflect the excitement that the wireless communication industry has. I want to the company to look exciting and attract new employees. The majority of our business is modifying and reinforcing existing cell towers to accept all the new tower top antennas that the increasing wireless mobile world demands.
Updates

I have added some sample photos from our business to our ArtBazaar profile.

We are now going through each design to find what is most suitable for our needs. Thank you all for your time in this matter.

Industry/Entity Type

Wireless Communication

```html
<!DOCTYPE html>
<html lang="en">
<head>
<meta charset="utf-8">
<title>TowerSpan, Inc.</title>
<link href="https://fonts.googleapis.com/css2?family=Lato:wght@400;700;900&family=Open+Sans:wght@400;600;700&display=swap" rel="stylesheet">
<style>
:root{
  --red:#c4161c;
  --red-dark:#a51217;
  --ink:#222;
  --text:#3a3a3a;
  --muted:#777;
  --line:#d8d8d8;
  --dark:#262626;
  --footer:#2b2b2b;
  --white:#fff;
}
*{box-sizing:border-box;margin:0;padding:0}
html,body{width:882px;height:1200px;overflow:hidden;background:var(--white)}
body{position:relative;font-family:Lato,sans-serif;color:var(--text)}
.abs{position:absolute}
a{color:inherit;text-decoration:none}

/* header */
.header{left:0;top:0;width:882px;height:78px;border-bottom:1px solid var(--line)}
.brand{left:98px;top:20px;display:flex;align-items:center;gap:8px}
.brand-dot{width:26px;height:26px;border-radius:50%;background:var(--red)}
.brand-name{font-size:29px;font-weight:400;color:var(--ink);letter-spacing:.3px}
.topline{right:104px;top:10px;display:flex;gap:14px;font-size:12.5px;color:#555;align-items:center}
.topline span{display:flex;align-items:center;gap:6px}
.topline .sep{width:1px;height:12px;background:var(--line)}
.nav{left:366px;top:46px;display:flex;align-items:center;font-size:11.5px;color:#333}
.nav a{padding:0 16px;border-left:1px solid var(--line);line-height:12px}
.nav a.active{background:var(--red);color:var(--white);border:none;line-height:23px;padding:0 10px;margin-right:6px;border-radius:2px}
.nav a.active + a{border-left:none}

/* hero */
.hero{left:0;top:78px;width:882px;height:275px;background:linear-gradient(180deg,#7fa6cf 0%,#a9c5e0 45%,#dbe6ef 75%,#b9cfe4 100%)}
.hero-tower{left:470px;top:78px;width:412px;height:275px;background:linear-gradient(120deg,rgba(90,100,110,0) 0%,rgba(80,90,100,.35) 40%,rgba(60,66,72,.55) 100%)}
.hero-kicker{left:96px;top:150px;font-size:20px;color:#1d1d1d;font-weight:700;white-space:nowrap}
.hero-kicker b{font-size:24px;font-weight:900}
.hero-title{left:96px;top:181px;height:34px;background:#3a3a3a;color:var(--white);font-size:22px;font-weight:700;line-height:34px;padding:0 10px;white-space:nowrap;letter-spacing:.2px}
.hero-sub{left:96px;top:218px;font-family:"Open Sans",sans-serif;font-size:11px;font-weight:600;color:#222;line-height:17px;white-space:nowrap}
.hero-btn{left:96px;top:260px;width:102px;height:27px;background:var(--red);color:var(--white);font-family:"Open Sans",sans-serif;font-weight:700;font-size:11.5px;line-height:27px;text-align:center;border-radius:2px}

/* services menu */
.menu{left:96px;top:374px;width:192px;background:var(--red);border-radius:2px;padding:0}
.menu li{list-style:none;height:27px;line-height:27px;font-family:"Open Sans",sans-serif;font-size:10.3px;color:var(--white);padding-left:26px;position:relative;border-bottom:1px solid var(--red-dark)}
.menu li::before{content:"›";position:absolute;left:13px;top:-1px;font-size:11px}
.menu li.active{background:#111;border-color:#111}

/* intro */
.intro-title{left:310px;top:372px;font-size:17.5px;color:#333;font-weight:400;white-space:nowrap}
.intro-title em{font-style:normal;color:var(--red)}
.intro-rule{left:310px;top:399px;width:475px;height:1px;background:var(--line)}
.intro-photo{left:310px;top:408px;width:136px;height:109px;background:linear-gradient(135deg,#5d6b3e,#8a948e 50%,#3b4a58)}
.intro-text{left:454px;top:408px;width:332px;font-size:9.5px;line-height:12.5px;color:#333}
.intro-more{left:310px;top:529px;width:476px;font-size:9.5px;line-height:12.5px;color:#333}
.btn{background:var(--red);color:var(--white);font-size:10.5px;text-align:center;border-radius:2px}
.intro-btn{left:310px;top:559px;width:71px;height:20px;line-height:20px}
.divider{left:120px;top:621px;width:640px;height:1px;background:linear-gradient(90deg,transparent,#ddd 30%,#ddd 70%,transparent)}

/* cards */
.card{top:642px;width:214px;height:218px;border:1px solid #e2e2e2;border-top:3px solid var(--dark);box-shadow:0 6px 8px -6px rgba(0,0,0,.25)}
.card h2{position:absolute;left:11px;top:10px;font-size:17.5px;font-weight:400;color:var(--red)}
.card-photo{left:10px;top:37px;width:194px;height:88px;background:linear-gradient(180deg,#e9ebee,#cfd3d8 60%,#3b3f47)}
.card-text{left:11px;top:136px;width:194px;font-size:9.6px;line-height:14.5px;color:#444}
.card-btn{left:11px;top:185px;width:72px;height:21px;line-height:21px}
.news{position:absolute;left:11px;width:192px}
.date{position:absolute;left:0;top:2px;width:27px;height:27px;background:#3a3a3a;color:var(--white);text-align:center;border-radius:2px}
.date b{display:block;font-size:10px;line-height:15px}
.date i{display:block;font-style:normal;font-size:6.5px;background:#555;line-height:11px}
.news-body{margin-left:35px;font-size:9.5px;line-height:14.5px;color:#444}
.news-body strong{color:#222}
.news-sep{left:11px;top:104px;width:190px;border-top:1px dotted #ccc}
.field{position:absolute;left:14px;width:185px;height:24px;border:1px solid #d3d3d3;border-radius:3px;font-size:9.5px;color:#666;display:flex;align-items:center;gap:7px;padding-left:8px}
.field.msg{height:47px;align-items:flex-start;padding-top:6px}

/* partners */
.partners{left:96px;top:894px;width:689px;height:91px;border:1px solid #dcdcdc}
.partners-tab{left:243px;top:-1px}
.partners-title{left:0;top:4px;width:689px;text-align:center;font-size:17px;color:var(--white)}
.badge{top:46px;height:22px;border-radius:11px;background:#c9c9c9}
.arrow{top:44px;font-size:22px;color:#555}

/* footer */
.footer{left:0;top:1020px;width:882px;height:154px;background:var(--footer);color:#e8e8e8}
.fcol{top:18px}
.fcol h3{font-size:15.5px;font-weight:400;color:var(--white);padding-bottom:6px;border-bottom:1px solid #4a4a4a;white-space:nowrap}
.links li{list-style:none;font-size:10.3px;line-height:17.2px;padding-left:10px;position:relative}
.links li::before{content:"›";position:absolute;left:0}
.contact-row{display:flex;gap:10px;font-size:10.3px;line-height:13.5px}
.nl-input{width:153px;height:19px;background:var(--white);border-radius:2px;font-size:7.5px;color:#888;line-height:19px;padding-left:6px}
.nl-btn{width:69px;height:19px;line-height:19px;background:var(--red);color:var(--white);font-size:9.5px;font-weight:700;text-align:center;border-radius:1px}
.social li{list-style:none;display:flex;align-items:center;gap:8px;font-size:10.3px;height:23.5px}
.social i{width:15px;height:15px;background:#f2f2f2;display:inline-block}
.copyright{left:0;top:1174px;width:882px;height:26px;background:var(--red);color:var(--white);font-size:10.5px;line-height:26px;text-align:center}
</style>
</head>
<body>

<header class="abs header">
  <div class="abs brand"><span class="brand-dot"></span><span class="brand-name">TowerSpan</span></div>
  <div class="abs topline">
    <span><svg width="11" height="11" viewBox="0 0 24 24"><path fill="#444" d="M6.6 10.8a15 15 0 0 0 6.6 6.6l2.2-2.2c.3-.3.7-.4 1-.2 1.1.4 2.3.6 3.6.6.6 0 1 .4 1 1V20c0 .6-.4 1-1 1A17 17 0 0 1 3 4c0-.6.4-1 1-1h3.5c.6 0 1 .4 1 1 0 1.3.2 2.5.6 3.6.1.3 0 .7-.2 1z"/></svg>(555) 014-2290</span>
    <span class="sep"></span>
    <span><svg width="11" height="9" viewBox="0 0 22 16"><rect x="0" y="0" width="22" height="16" fill="#444"/><path d="M0 0l11 9 11-9" fill="none" stroke="#fff" stroke-width="1.6"/></svg>info@towerspanco.net</span>
  </div>
  <nav class="abs nav">
    <a class="active" href="#">Home</a><a href="#">About Us</a><a href="#">Services</a><a href="#">Projects</a><a href="#">News</a><a href="#">Contact Us</a>
  </nav>
</header>

<section class="abs hero" role="img" aria-label="Sky with clouds behind a steel communication tower"></section>
<div class="abs hero-tower" role="img" aria-label="Tower technician climbing a lattice steel tower"></div>
<div class="abs hero-kicker">We are regarded as <b>PIONEERS</b> in the</div>
<div class="abs hero-title">COMMUNICATIONS INDUSTRY</div>
<div class="abs hero-sub">experienced and innovative provider of communication towers,<br>tower reinforcements and related support services.</div>
<a class="abs hero-btn" href="#">LEARN MORE</a>

<ul class="abs menu">
  <li>Tower Reinforcement</li>
  <li>Rapid Deployment Site</li>
  <li>Towers</li>
  <li class="active">Monopole Reinforcement</li>
  <li>Tower Accessories</li>
  <li>Custom Steel Fabrication</li>
  <li>Antenna Support Structures</li>
  <li>Contruction Services</li>
</ul>

<h1 class="abs intro-title">TowerSpan, Inc. <em>Towering above the rest</em></h1>
<div class="abs intro-rule"></div>
<div class="abs intro-photo" role="img" aria-label="Technician in safety harness working on a monopole"></div>
<p class="abs intro-text">TowerSpan, Inc., is an experienced and innovative provider of communication towers, tower reinforcements and related support services. Specializing in the manufacturing, installation, and maintenance of communication infrastructure products, we are regarded as pioneers in the communications industry. From the innovative structural design ideas we develop for antenna systems and tower reinforcements, to the alternative tower installation techniques we offer, TowerSpan consistently delivers high quality solutions for the commercial, defense, federal, and international markets..</p>
<p class="abs intro-more">We invite you to explore our website, then contact us; so that we may begin to develop and implement the superior, cost effective, and timely solutions that your individual project requires.</p>
<a class="abs btn intro-btn" href="#">Read More</a>
<div class="abs divider"></div>

<section class="abs card" style="left:96px">
  <h2>What we do</h2>
  <div class="abs card-photo" role="img" aria-label="Team of business professionals in an office"></div>
  <p class="abs card-text">Hendrerit in vulputate molestie consqua sisi atvero eros et accumsan iustoodi dignissimr qui blandit praesent luptatulenit</p>
  <a class="abs btn card-btn" href="#">Read More</a>
</section>

<section class="abs card" style="left:334px">
  <h2>Latest News</h2>
  <div class="news" style="top:38px">
    <div class="date"><b>22</b><i>JULY</i></div>
    <p class="news-body"><strong>Vero eros accumsaet odio</strong><br>quis nostrud exetiperj lipsususcipit lobtis nisl ut aliquip ex ea commod Lorem Ipsum is simply dummy.</p>
  </div>
  <div class="abs news-sep"></div>
  <div class="news" style="top:111px">
    <div class="date"><b>22</b><i>JULY</i></div>
    <p class="news-body"><strong>Eros accumsaet iusto odio</strong><br>quis nostrud exetiperj lipsususcipit lobtis nisl ut aliquip ex ea commod Lorem Ipsum is simply dummy.</p>
  </div>
  <a class="abs btn card-btn" href="#">Read More</a>
</section>

<section class="abs card" style="left:571px">
  <h2>Quick Contact</h2>
  <div class="field" style="top:37px"><svg width="10" height="10" viewBox="0 0 10 10"><circle cx="5" cy="3" r="2.4" fill="#999"/><path d="M0 10c0-3 2.2-4.5 5-4.5S10 7 10 10z" fill="#999"/></svg>Name</div>
  <div class="field" style="top:66px"><svg width="10" height="8" viewBox="0 0 22 16"><rect width="22" height="16" fill="#999"/><path d="M0 0l11 9 11-9" fill="none" stroke="#fff" stroke-width="2"/></svg>Email</div>
  <div class="field" style="top:96px"><svg width="10" height="10" viewBox="0 0 24 24"><path fill="#999" d="M6.6 10.8a15 15 0 0 0 6.6 6.6l2.2-2.2c.3-.3.7-.4 1-.2 1.1.4 2.3.6 3.6.6.6 0 1 .4 1 1V20c0 .6-.4 1-1 1A17 17 0 0 1 3 4c0-.6.4-1 1-1h3.5c.6 0 1 .4 1 1 0 1.3.2 2.5.6 3.6.1.3 0 .7-.2 1z"/></svg>Phone Number</div>
  <div class="field msg" style="top:126px"><svg width="10" height="10" viewBox="0 0 10 10"><rect x=".5" y="1.5" width="7" height="8" fill="none" stroke="#999"/><path d="M4 6l5-5" stroke="#999" stroke-width="1.4"/></svg>Message</div>
  <a class="abs btn card-btn" href="#" style="left:13px;width:66px">Submit</a>
</section>

<section class="abs partners">
  <svg class="abs partners-tab" width="203" height="29" viewBox="0 0 203 29"><path d="M0 0h203l-18 25c-2 3-5 4-8 4H26c-3 0-6-1-8-4z" fill="#7a7a7a"/></svg>
  <div class="abs partners-title">Our Partners</div>
  <span class="abs arrow" style="left:14px">‹</span>
  <div class="abs badge" style="left:38px;width:110px"></div>
  <div class="abs badge" style="left:171px;width:102px"></div>
  <div class="abs badge" style="left:296px;width:102px"></div>
  <div class="abs badge" style="left:421px;width:104px"></div>
  <div class="abs badge" style="left:549px;width:101px"></div>
  <span class="abs arrow" style="left:664px">›</span>
</section>

<footer class="abs footer">
  <div class="abs fcol" style="left:104px;width:92px">
    <h3>Quick Links</h3>
    <ul class="links" style="margin-top:6px">
      <li>Home</li><li>About Us</li><li>Services</li><li>Projects</li><li>News</li><li>Contact Us</li>
    </ul>
  </div>
  <div class="abs fcol" style="left:232px;width:175px">
    <h3>Contact Information</h3>
    <div class="contact-row" style="margin-top:9px"><svg width="9" height="12" viewBox="0 0 10 14"><path d="M5 0a5 5 0 0 1 5 5c0 3.5-5 9-5 9S0 8.5 0 5a5 5 0 0 1 5-5z" fill="#eee"/><circle cx="5" cy="5" r="1.8" fill="#2b2b2b"/></svg><span>TowerSpan, Inc.<br>240 W. Harbor Lane<br>Pensacola, Florida 32500</span></div>
    <div class="contact-row" style="margin-top:10px"><svg width="10" height="10" viewBox="0 0 24 24"><path fill="#eee" d="M6.6 10.8a15 15 0 0 0 6.6 6.6l2.2-2.2c.3-.3.7-.4 1-.2 1.1.4 2.3.6 3.6.6.6 0 1 .4 1 1V20c0 .6-.4 1-1 1A17 17 0 0 1 3 4c0-.6.4-1 1-1h3.5c.6 0 1 .4 1 1 0 1.3.2 2.5.6 3.6.1.3 0 .7-.2 1z"/></svg><span>(555) 014-2290</span></div>
    <div class="contact-row" style="margin-top:10px"><svg width="10" height="8" viewBox="0 0 22 16" style="margin-top:3px"><rect width="22" height="16" fill="#eee"/><path d="M0 0l11 9 11-9" fill="none" stroke="#2b2b2b" stroke-width="2"/></svg><span>info@towerspanco.net</span></div>
  </div>
  <div class="abs fcol" style="left:446px;width:164px">
    <h3>Newsletter Sign Up</h3>
    <p style="font-size:10.3px;line-height:14px;margin-top:7px">Lorem ipsudolor sit coec adipiscing elitsite amet</p>
    <div class="nl-input" style="margin-top:6px">Email Address</div>
    <div class="nl-btn" style="margin-top:9px">SUBSCRIBE</div>
  </div>
  <div class="abs fcol" style="left:646px;width:132px">
    <h3>Follow Us</h3>
    <ul class="social" style="margin-top:6px">
      <li><i></i>Friendly</li><li><i></i>Chirper</li><li><i></i>PlusCircle</li><li><i></i>WorkLink</li>
    </ul>
  </div>
</footer>
<div class="abs copyright">Copyright © 2014 TowerSpan Inc. All Rights Reserved</div>

</body>
</html>
```